Bolvarin Incorporated

Bolvarin is a business that provides consulting, and manages and supplies trades persons in the construction and heavy industries sector. We build, do maintenance, install machinery, and can manage projects or jobs. Would like or prefer more clean, classic designs. Blacks/greys, but open to almost anything.

Target Market(s)

Industrial/Construction/Manufacturing

Industry/Entity Type

Construction Company

Contact Information for Business Card

Clean, business name on the front, possibly have the details on the back, but open to any ideas.

Logo Text

We currently do not have a slogan, open to ideas

Font styles to use
Serif
Sans Serif

Colors

Designer to choose colors to be used in the design.

Requirements
Should not have
• the oval is not my logo, was just an idea. please don't send 20 designs with the oval

```html
<!DOCTYPE html>
<html lang="en">
<head>
<meta charset="utf-8">
<title>Bolvarin Business Card</title>
<link rel="stylesheet" href="https://fonts.googleapis.com/css2?family=Josefin+Sans:wght@300;400&family=Cormorant+SC:wght@700&family=Montserrat:wght@400&display=swap">
<style>
  :root {
    --page-bg: #1c1c1e;
    --card-front: #62626e;
    --card-back: #ffffff;
    --accent: #f6ad2c;
    --ink: #5a5a63;
    --ink-light: #6e6e76;
    --white: #ffffff;
  }
  * { margin: 0; padding: 0; box-sizing: border-box; }
  html, body {
    width: 1200px; height: 900px; overflow: hidden;
    background: var(--page-bg);
  }
  .sheet {
    width: 1200px; height: 900px;
    display: flex; flex-direction: column; align-items: center; justify-content: center;
    gap: 40px;
  }
  .card {
    position: relative;
    width: 665px; height: 380px;
    overflow: hidden;
  }
  .card--front { background: var(--card-front); }
  .card--back { background: var(--card-back); }

  .wordmark {
    font-family: "Josefin Sans", sans-serif;
    font-weight: 300;
    text-transform: uppercase;
    letter-spacing: 0.12em;
    white-space: nowrap;
  }
  .card--front .wordmark {
    position: absolute; left: 0; right: 0; top: 50%;
    transform: translateY(-50%);
    text-align: center;
    font-size: 60px;
    color: var(--white);
  }
  .card--back .wordmark {
    position: absolute; right: 48px; top: 52px;
    font-size: 40px;
    color: var(--ink);
  }
  .divider {
    position: absolute; left: 0; right: 0; top: 110px;
    height: 2px; background: var(--accent);
  }
  .holder {
    position: absolute; left: 312px; top: 130px;
  }
  .holder__name {
    font-family: "Cormorant SC", serif;
    font-weight: 700;
    font-size: 26px;
    letter-spacing: 0.06em;
    color: var(--accent);
    line-height: 1;
  }
  .holder__role {
    font-family: "Montserrat", sans-serif;
    font-size: 16px;
    color: var(--ink-light);
    margin-top: 2px;
  }
  .contacts {
    position: absolute; left: 300px; top: 204px;
    list-style: none;
    font-family: "Montserrat", sans-serif;
    font-size: 18px;
    color: var(--ink);
  }
  .contacts__item {
    display: flex; align-items: center; gap: 10px;
    height: 27px;
  }
  .contacts__icon { width: 17px; height: 17px; flex: none; }
  .address {
    position: absolute; left: 268px; top: 306px;
    font-family: "Montserrat", sans-serif;
    font-size: 19px;
    color: var(--ink);
  }
</style>
</head>
<body>
<main class="sheet">
  <section class="card card--front" aria-label="Card front">
    <div class="wordmark">Bolvarin</div>
  </section>

  <section class="card card--back" aria-label="Card back">
    <div class="wordmark">Bolvarin</div>
    <div class="divider"></div>
    <div class="holder">
      <div class="holder__name">Dorian Pell</div>
      <div class="holder__role">Sales Manager</div>
    </div>
    <ul class="contacts">
      <li class="contacts__item">
        <svg class="contacts__icon" viewBox="0 0 20 20" aria-hidden="true">
          <circle cx="10" cy="10" r="8.5" fill="none" stroke="#f6ad2c" stroke-width="1.5"/>
          <path d="M7 5.5l1.6 0 .8 2.4-1.1.8a6 6 0 0 0 2.9 2.9l.8-1.1 2.4.8v1.6c0 .6-.5 1-1.1 1A7.5 7.5 0 0 1 6 6.6c0-.6.4-1.1 1-1.1z" fill="#f6ad2c"/>
        </svg>
        <span>555-210-4837</span>
      </li>
      <li class="contacts__item">
        <svg class="contacts__icon" viewBox="0 0 20 20" aria-hidden="true">
          <rect x="2" y="4.5" width="16" height="11" fill="none" stroke="#f6ad2c" stroke-width="1.5"/>
          <path d="M2 4.5l8 6.5 8-6.5" fill="none" stroke="#f6ad2c" stroke-width="1.5"/>
        </svg>
        <span>info@bolvarin.com</span>
      </li>
      <li class="contacts__item">
        <svg class="contacts__icon" viewBox="0 0 20 20" aria-hidden="true">
          <circle cx="10" cy="10" r="8.5" fill="#f6ad2c"/>
          <path d="M1.5 10h17M10 1.5c-3 3-3 14 0 17M10 1.5c3 3 3 14 0 17M3 6h14M3 14h14" fill="none" stroke="#ffffff" stroke-width="1"/>
        </svg>
        <span>www.bolvarin.com</span>
      </li>
    </ul>
    <p class="address">PO Box 318, Ravenmoor. Qld 4702</p>
  </section>
</main>
</body>
</html>
```